Kestrelwood Pathways Agency business cards

Australian company about to start offering its services. We recruit international students to come to study English, vocational education and postgraduate courses in Australia. We help them find the institution and select the right city they want to come to Australia. We are a young, online oriented and supportive agency. Our clients are between 18 and 35 years old, mainly University students, young professionals or people with work experience. We provide much more information that any other agency offer. We administrate a Facebook group with more than 11.000 members that daily ask questions about general information when coming to Australia, while they are here and even after they leave the country

Target Market(s)

International students from South America, Central America and Europe

Industry/Entity Type

Student

Contact Information for Business Card

Tomas Brevik
Managing Director
tomas@velmorin.com.au
www.velmorin.com.au
+61 491058263
Melbourne, Australia

Font styles to use
Serif
Sans Serif

Colors

Designer to choose colors to be used in the design.

Requirements
Must have
• Horizontal design
• Standard business card size and shape. If font uses green or yellow colours, they will have to match the ones from the logo
Nice to have
• UPDATE: Use the contents of the green image to design one of the card sides. Use our logo in the background of that side as watermark.
• Passport image, or immigration stamps. A picture of the Yarra River (from Melbourne) would be cool as well.
Should not have
• Non-standard business card size and shape
• Not black as the background colour of any sides as we are not a VIP agency or a hight class service. We are orientes to young people and they like colours, pictures, something attractive.
• Vertical design
• NO YELLOW or BLACK AS THE BACKGROUND COLOUR OF ANY SIDE OF THE BIZ CARD

```html
<!DOCTYPE html>
<html lang="en">
<head>
<meta charset="utf-8">
<title>Kestrelwood Pathways Agency — Business Cards</title>
<link rel="stylesheet" href="https://fonts.googleapis.com/css2?family=Jost:wght@400;500;600&display=swap">
<style>
  :root {
    --backdrop: #cbcbcb;
    --card-white: #ffffff;
    --brand-green: #0f5a36;
    --card-green: #176044;
    --ink: #3a3a3a;
    --on-green: #ffffff;
  }
  * { box-sizing: border-box; margin: 0; padding: 0; }
  html, body {
    width: 1200px;
    height: 1000px;
    overflow: hidden;
    background: var(--backdrop);
    font-family: "Jost", "Futura", sans-serif;
  }
  .card {
    position: absolute;
    left: 295px;
    width: 587px;
    height: 335px;
  }
  .card--front { top: 149px; background: var(--card-white); }
  .card--back { top: 517px; background: var(--card-green); }

  .holder { position: absolute; left: 44px; top: 60px; }
  .holder__name {
    font-size: 23px;
    font-weight: 600;
    letter-spacing: 0.8px;
    color: var(--brand-green);
    line-height: 1;
  }
  .holder__role {
    margin-top: 4px;
    font-size: 15px;
    font-weight: 400;
    letter-spacing: 0.4px;
    color: var(--ink);
  }

  .wordmark {
    position: absolute;
    display: flex;
    align-items: center;
    gap: 8px;
    font-weight: 500;
    line-height: 1;
  }
  .wordmark__dot { border-radius: 50%; flex: none; }
  .card--front .wordmark {
    right: 46px;
    top: 76px;
    font-size: 30px;
    color: var(--brand-green);
  }
  .card--front .wordmark__dot { width: 12px; height: 12px; background: var(--brand-green); }
  .card--back .wordmark {
    left: 50%;
    top: 128px;
    transform: translateX(-50%);
    font-size: 54px;
    color: var(--on-green);
  }
  .card--back .wordmark__dot { width: 18px; height: 18px; background: var(--on-green); }

  .contacts {
    position: absolute;
    left: 44px;
    top: 250px;
    list-style: none;
  }
  .contacts__item {
    display: flex;
    align-items: center;
    height: 19px;
    font-size: 13.5px;
    letter-spacing: 0.6px;
    color: var(--ink);
  }
  .contacts__icon {
    width: 11px;
    height: 11px;
    margin-right: 9px;
    flex: none;
    fill: var(--brand-green);
    stroke: var(--brand-green);
  }

  .location {
    position: absolute;
    right: 47px;
    top: 269px;
    text-align: right;
    font-size: 13.5px;
    letter-spacing: 0.9px;
    line-height: 19px;
    color: var(--ink);
  }

  .tagline {
    position: absolute;
    left: 0;
    right: 0;
    top: 288px;
    text-align: center;
    font-size: 14px;
    font-weight: 500;
    letter-spacing: 0.6px;
    color: var(--on-green);
  }
</style>
</head>
<body>

<section class="card card--front" aria-label="Business card front">
  <div class="holder">
    <h1 class="holder__name">TOMAS BREVIK</h1>
    <p class="holder__role">Managing Director</p>
  </div>

  <div class="wordmark"><span class="wordmark__dot"></span>Velmorin</div>

  <ul class="contacts">
    <li class="contacts__item">
      <svg class="contacts__icon" viewBox="0 0 11 11" aria-hidden="true">
        <rect x="2.5" y="0.8" width="6" height="9.4" rx="1" fill="none" stroke-width="1.4"/>
        <rect x="4.6" y="8" width="1.8" height="0.9" stroke="none"/>
      </svg>
      +61 491058263
    </li>
    <li class="contacts__item">
      <svg class="contacts__icon" viewBox="0 0 11 11" aria-hidden="true">
        <rect x="0.5" y="2" width="10" height="7" rx="0.8" stroke="none"/>
        <polyline points="0.8,2.4 5.5,6 10.2,2.4" fill="none" stroke="#fff" stroke-width="1"/>
      </svg>
      tomas@velmorin.com.au
    </li>
    <li class="contacts__item">
      <svg class="contacts__icon" viewBox="0 0 11 11" aria-hidden="true">
        <circle cx="4.5" cy="4.5" r="3.2" fill="none" stroke-width="1.6"/>
        <line x1="6.8" y1="6.8" x2="10" y2="10" stroke-width="1.9" stroke-linecap="round"/>
      </svg>
      www.velmorin.com.au
    </li>
  </ul>

  <p class="location">Melbourne,<br>Australia</p>
</section>

<section class="card card--back" aria-label="Business card back">
  <div class="wordmark"><span class="wordmark__dot"></span>Velmorin</div>
  <p class="tagline">Hacemos más por ti!</p>
</section>

</body>
</html>
```